New name flyer

We have just changed our business name from kR Property group to Harbour Lantern. We want to distribute a flyer to the local community to inform them of the change. We are a realestate agency which focuses mainly on property management but also sales. We service from Brisbane to the Sunshine coast.

Target Market(s)

Local community

Industry/Entity Type

realestate

Requirements
Must have
• Details of name change
Nice to have
• Servicing area Brisbane and Sunshine Coast, no change in management or services we offer, and will continue pride ourselves on offering a high level of service, with the same team from the Gold to Sunshine Coast.
Should not have
• too much wording.

```html
<!DOCTYPE html>
<html lang="en">
<head>
<meta charset="utf-8">
<title>Harbour Lantern – New Name Flyer</title>
<link rel="stylesheet" href="https://fonts.googleapis.com/css2?family=Raleway:wght@600;700;800&family=Roboto+Condensed:wght@400;700&display=swap">
<style>
  :root {
    --navy: #1e3461;
    --gold: #c99a33;
    --white: #ffffff;
    --grey: #6f6f73;
    --rule: #d4d4d4;
    --photo-sky: #cfdbe6;
    --photo-house: #9a8a78;
    --photo-lawn: #7c8c5a;
  }
  * { margin: 0; padding: 0; box-sizing: border-box; }
  html, body { width: 849px; height: 1200px; overflow: hidden; background: var(--white); }
  .flyer { position: relative; width: 849px; height: 1200px; overflow: hidden; background: var(--white); font-family: "Roboto Condensed", "Arial Narrow", sans-serif; }
  .shapes { position: absolute; inset: 0; }

  .brand { position: absolute; left: 39px; top: 96px; }
  .brand-name { font-family: "Raleway", sans-serif; font-weight: 800; font-size: 35px; line-height: 36px; color: var(--navy); letter-spacing: 0.5px; }
  .brand-tag { margin-top: 10px; font-family: "Raleway", sans-serif; font-weight: 600; font-size: 15px; letter-spacing: 6.5px; color: var(--gold); }

  .name-change { position: absolute; right: 38px; top: 58px; text-align: right; font-family: "Raleway", sans-serif; font-weight: 700; font-size: 22px; line-height: 28px; color: var(--navy); }
  .name-change .accent { color: var(--gold); }

  .service-title { position: absolute; right: 464px; top: 262px; text-align: right; font-family: "Roboto Condensed", sans-serif; font-weight: 700; font-size: 47px; line-height: 54px; color: var(--white); letter-spacing: 0.5px; }

  .service-list { position: absolute; left: 16px; top: 396px; width: 300px; list-style: none; color: var(--white); font-size: 15.5px; line-height: 20px; }
  .service-list li { position: relative; padding-left: 13px; margin-bottom: 20px; }
  .service-list li::before { content: ""; position: absolute; left: 0; top: 8px; width: 5px; height: 5px; border-radius: 50%; background: var(--white); }

  .headline { position: absolute; left: 0; top: 798px; width: 356px; text-align: center; font-weight: 700; font-size: 47px; line-height: 45px; color: var(--navy); letter-spacing: 0.5px; }
  .headline .accent { color: var(--gold); }

  .why-title { position: absolute; right: 33px; top: 784px; font-family: "Raleway", sans-serif; font-weight: 600; font-size: 29px; color: var(--navy); letter-spacing: 0.5px; }
  .why-body { position: absolute; right: 30px; top: 840px; width: 446px; text-align: right; font-size: 15.2px; line-height: 19.4px; color: var(--grey); }

  .contacts { position: absolute; left: 32px; top: 1034px; list-style: none; }
  .contacts li { display: flex; align-items: center; height: 45px; font-size: 21px; color: var(--grey); }
  .contacts svg { width: 22px; height: 22px; margin-right: 12px; flex: none; }

  .call { position: absolute; right: 30px; top: 1083px; display: flex; align-items: center; font-weight: 700; font-size: 25px; color: var(--white); }
  .call svg { width: 30px; height: 30px; margin-right: 8px; }
  .phone { position: absolute; right: 30px; top: 1122px; font-family: "Raleway", sans-serif; font-weight: 600; font-size: 35px; color: var(--white); letter-spacing: 0.5px; }
</style>
</head>
<body>
<main class="flyer">
  <svg class="shapes" viewBox="0 0 655 926" width="849" height="1200">
    <defs>
      <linearGradient id="photoTone" x1="0" y1="0" x2="0" y2="1">
        <stop offset="0" stop-color="var(--photo-sky)"/>
        <stop offset="0.35" stop-color="#b7c3cf"/>
        <stop offset="0.55" stop-color="var(--photo-house)"/>
        <stop offset="0.82" stop-color="#a7a39a"/>
        <stop offset="1" stop-color="var(--photo-lawn)"/>
      </linearGradient>
    </defs>
    <polygon points="0,272 312,130 312,292 254,525 0,620" fill="var(--gold)"/>
    <line x1="120" y1="292" x2="312" y2="292" stroke="var(--white)" stroke-width="2"/>
    <line x1="0" y1="530" x2="160" y2="530" stroke="var(--white)" stroke-width="2"/>
    <polygon role="img" aria-label="Photo of a two-storey brick and weatherboard family home with a double garage and front lawn" points="312,292 655,125 655,462 340,640 254,640 254,525" fill="url(#photoTone)"/>
    <line x1="312" y1="292" x2="655" y2="125" stroke="var(--rule)" stroke-width="3"/>
    <polygon points="340,640 655,462 655,500" fill="var(--navy)"/>
    <line x1="410" y1="634" x2="655" y2="634" stroke="var(--navy)" stroke-width="2"/>
    <polygon points="225,926 445,823 445,848 278,926" fill="var(--gold)"/>
    <polygon points="290,926 655,748 655,926" fill="var(--navy)"/>
  </svg>

  <div class="brand">
    <div class="brand-name">HARBOUR<br>LANTERN</div>
    <div class="brand-tag">ESTATE AGENTS</div>
  </div>

  <p class="name-change">WE ARE NOW FROM<br><span class="accent">KR PROPERTY GROUP</span><br>TO <span class="accent">HARBOUR LANTERN</span></p>

  <h1 class="service-title">PROPERTY<br>MANAGEMENT</h1>

  <ul class="service-list">
    <li>Lorem Ipsum Is Simply Dummy Text Of The Printing And Typesetting Industry.</li>
    <li>Lorem Ipsum Is Simply Dummy Text Of The Printing And Typesetting Industry.</li>
    <li>Lorem Ipsum is simply dummy text of the printing and typesetting industry.<br>It has survived not only five centuries, but also the leap into electronic typesetting.</li>
    <li>Lorem Ipsum Is Simply Dummy Text Of The Printing And Typesetting Industry.</li>
  </ul>

  <h2 class="headline">READY TO<br>SERVE<br><span class="accent">YOUR DREAM<br>HOUSE</span></h2>

  <h3 class="why-title">WHY CHOOSE US</h3>
  <p class="why-body">There are many variations of passages of Lorem Ipsum available, but the majority have suffered alteration in some form, by injected humour, or randomised words which don't look even slightly believable. If you are going to use a passage of Lorem Ipsum, you need to be sure there isn't anything embarrassing hidden in the middle of text. All the Lorem Ipsum generators on the Internet tend to repeat predefined chunks as necessary</p>

  <ul class="contacts">
    <li><svg viewBox="0 0 22 22"><circle cx="11" cy="11" r="11" fill="var(--navy)"/><rect x="5.5" y="7" width="11" height="8" fill="none" stroke="var(--white)" stroke-width="1.5"/><polyline points="5.5,7 11,11.5 16.5,7" fill="none" stroke="var(--white)" stroke-width="1.5"/></svg>E-MAIL ADDRESS WILL GO HERE</li>
    <li><svg viewBox="0 0 22 22"><circle cx="11" cy="11" r="11" fill="var(--navy)"/><line x1="3" y1="8" x2="19" y2="8" stroke="var(--white)" stroke-width="1.5"/><line x1="2" y1="11" x2="20" y2="11" stroke="var(--white)" stroke-width="1.5"/><line x1="3" y1="14" x2="19" y2="14" stroke="var(--white)" stroke-width="1.5"/></svg>WEB ADDRESS WILL GO HERE</li>
    <li><svg viewBox="0 0 22 22"><circle cx="11" cy="11" r="11" fill="var(--navy)"/><path d="M6 11 L11 6.5 L16 11 V16 H6 Z" fill="none" stroke="var(--white)" stroke-width="1.5"/><circle cx="11" cy="12" r="1.6" fill="var(--white)"/></svg>ADDRESS WILL GO HERE</li>
  </ul>

  <div class="call"><svg viewBox="0 0 30 30"><circle cx="15" cy="15" r="15" fill="var(--white)"/><path d="M10 8 l3 0 l1.5 4 l-2 1.5 a9 9 0 0 0 4 4 l1.5 -2 l4 1.5 l0 3 a2 2 0 0 1 -2 2 a13 13 0 0 1 -12 -12 a2 2 0 0 1 2 -2 z" fill="var(--navy)"/></svg>CALL US:</div>
  <p class="phone">012 345 6789</p>
</main>
</body>
</html>
```